Redesign Fitness Photos for Facebook Ads Needed

We are a fun, energetic, group fitness facility that needs to have a few (3) photos doctored up and turned into ads for Facebook & Instagram.
I would like the photos to be doctored up so that they are clear, bright, energetic.  Feel free to manipulate the photos, backgrounds, cropping, cutting as needed.
I would like to include text on photos:
PulVora
New Year
Challenge
* Fitness Training  * Nutritional Support * Motivation & Support
Join Now
The text should be roughly the size of the examples included in order to comply with facebooks text size requirements
I have included 3 examples of another gyms ads which I like how the images are eye catching and text is clearly visible and pops with color.
Although I have attached multiple images that can be used,  I am only looking for 3 completed designs to be used for ads.

You choose the images that you feel you can modify the best.
I look forward to seeing your design.
Thank you.

```html
<!DOCTYPE html>
<html lang="en">
<head>
<meta charset="UTF-8">
<title>PulVora – New Year Challenge</title>
<link rel="stylesheet" href="https://fonts.googleapis.com/css2?family=Bungee&family=Titan+One&family=Poppins:ital,wght@0,500;0,800;1,800&display=swap">
<style>
  :root {
    --white: #ffffff;
    --ink: #111316;
    --lime: #b3cc12;
    --lime-pale: #e6efcf;
    --orange: #ffb400;
    --purple: #2e00db;
    --bullet: #e4f03a;
    --logo: #24282f;
    --tagline: #4a4d52;
    --photo-top: #b2566e;
    --photo-mid: #8a1f3c;
    --photo-bottom: #2a2b30;
  }
  html, body {
    margin: 0;
    padding: 0;
    width: 1200px;
    height: 1200px;
    overflow: hidden;
    background: var(--white);
  }
  .ad {
    position: relative;
    width: 1200px;
    height: 1200px;
    overflow: hidden;
    background: var(--white);
  }
  .ad-shapes {
    position: absolute;
    inset: 0;
  }
  .brand {
    position: absolute;
    left: 100px;
    top: 76px;
  }
  .brand-name {
    font-family: "Poppins", sans-serif;
    font-weight: 800;
    font-size: 88px;
    line-height: 1;
    color: var(--logo);
    letter-spacing: -1px;
  }
  .brand-tagline {
    margin-top: 6px;
    font-family: "Poppins", sans-serif;
    font-weight: 500;
    font-size: 22px;
    letter-spacing: 4px;
    color: var(--tagline);
  }
  .join-button {
    position: absolute;
    left: 50px;
    top: 408px;
    width: 324px;
    height: 98px;
    border-radius: 14px;
    background: var(--lime);
    color: var(--white);
    font-family: "Titan One", sans-serif;
    font-size: 54px;
    line-height: 98px;
    text-align: center;
    letter-spacing: 1px;
  }
  .headline {
    position: absolute;
    left: 36px;
    top: 692px;
    margin: 0;
    font-family: "Bungee", sans-serif;
    font-weight: 400;
    font-size: 100px;
    line-height: 114px;
    color: var(--white);
    transform: skewX(-12deg);
    transform-origin: left bottom;
    text-shadow: 6px 5px 0 var(--orange);
    letter-spacing: 1px;
  }
  .benefits {
    position: absolute;
    left: 33px;
    top: 1004px;
    margin: 0;
    padding: 0;
    list-style: none;
  }
  .benefits li {
    position: relative;
    padding-left: 70px;
    height: 48px;
    font-family: "Poppins", sans-serif;
    font-style: italic;
    font-weight: 800;
    font-size: 30px;
    line-height: 48px;
    color: var(--bullet);
  }
  .benefits li::before {
    content: "";
    position: absolute;
    left: 0;
    top: 21px;
    width: 36px;
    height: 6px;
    border-radius: 3px;
    background: var(--bullet);
  }
</style>
</head>
<body>
<main class="ad">
  <svg class="ad-shapes" width="1200" height="1200" viewBox="0 0 1200 1200">
    <defs>
      <linearGradient id="photo-tone" x1="0" y1="0" x2="0" y2="1">
        <stop offset="0" stop-color="var(--photo-top)"/>
        <stop offset="0.4" stop-color="var(--photo-mid)"/>
        <stop offset="0.75" stop-color="var(--photo-bottom)"/>
        <stop offset="1" stop-color="#1b1c20"/>
      </linearGradient>
    </defs>
    <polygon class="stripe-pale" points="700,0 820,0 760,80 640,80" fill="var(--lime-pale)"/>
    <polygon class="stripe-pale" points="1000,0 1200,0 1200,40 880,470 780,470" fill="var(--lime-pale)"/>
    <polygon class="stripe-lime" points="1110,0 1200,0 1200,40 900,385 805,385" fill="var(--lime)"/>
    <polygon class="stripe-pale" points="1200,300 1200,640 1060,640" fill="var(--lime-pale)"/>
    <g class="dots-orange" fill="var(--orange)">
      <circle cx="952" cy="69" r="9"/><circle cx="1010" cy="69" r="9"/><circle cx="1067" cy="69" r="9"/><circle cx="1125" cy="69" r="9"/>
      <circle cx="952" cy="123" r="9"/><circle cx="1010" cy="123" r="9"/><circle cx="1067" cy="123" r="9"/><circle cx="1125" cy="123" r="9"/>
      <circle cx="952" cy="177" r="9"/><circle cx="1010" cy="177" r="9"/><circle cx="1067" cy="177" r="9"/><circle cx="1125" cy="177" r="9"/>
    </g>
    <polygon class="stripe-pale" points="0,300 0,350 260,650 300,650" fill="var(--lime-pale)"/>
    <polygon class="stripe-ink" points="0,232 0,420 150,520 300,520" fill="var(--ink)"/>
    <polygon class="stripe-lime" points="0,470 0,520 120,648 170,648" fill="var(--lime)"/>
    <g class="dots-ink" fill="var(--ink)">
      <circle cx="106" cy="548" r="6"/><circle cx="140" cy="548" r="6"/><circle cx="175" cy="548" r="6"/><circle cx="210" cy="548" r="6"/>
      <circle cx="106" cy="582" r="6"/><circle cx="140" cy="582" r="6"/><circle cx="175" cy="582" r="6"/><circle cx="210" cy="582" r="6"/>
      <circle cx="106" cy="616" r="6"/><circle cx="140" cy="616" r="6"/><circle cx="175" cy="616" r="6"/><circle cx="210" cy="616" r="6"/>
    </g>
    <polygon class="banner-ink" points="0,648 958,648 712,978 0,978" fill="var(--ink)"/>
    <polygon class="stripe-lime" points="1200,760 1200,1105 980,1105" fill="var(--lime)"/>
    <rect class="band-purple" x="0" y="974" width="1200" height="226" fill="var(--purple)"/>
    <line x1="820" y1="1170" x2="1010" y2="975" stroke="#4b2bff" stroke-width="2"/>
    <rect class="photo" role="img" aria-label="Photo of a woman in a red tank top training with battle ropes"
      x="780" y="250" width="370" height="950" rx="24" fill="url(#photo-tone)"/>
  </svg>

  <header class="brand">
    <div class="brand-name">PulVora</div>
    <div class="brand-tagline">Personal Group Training</div>
  </header>

  <div class="join-button">JOIN NOW</div>

  <h1 class="headline">NEW YEAR<br>CHALLENGE</h1>

  <ul class="benefits">
    <li>FITNESS TRAINING</li>
    <li>NUTRITIONAL SUPPORT</li>
    <li>MOTIVATION &amp; SUPPORT</li>
  </ul>
</main>
</body>
</html>
```